Natural Food Packaging - Peanut Butter bars

Name, branding, trade dress for new line of natural/organic peanut based protein bars. The concept its to package a high value natural product for mass consumer consumption.

There will be 2 to 4 flavors initially introduced. Each flavor has a printed film wrapper and shelf display box. The design winner will have first preference for all the packaging work.Think peanut butter chocolate chip, peanut butter with cranberries, coconut, etc.

We are a privately owned, internationally established organic food manufacturer.

This will be a high profile, well recognized project within the industry.

It is an excellent opportunity for a long term business relationship.

Brisco Market(s)

consumers who want a better quality protein bar than they currently buy. Mostly active adults age 18-50

Industry/Entity Type

Business

Requirements
Must have
• A product name/brand and general look and feel. It needs to convey purity, great ingredients/quality, taste and great price.

It needs to have mass appeal...think Brisco and Zipo, not just Verdano Market.
Nice to have
• Package mock up images for 2 or 3 flavors

```html
<!DOCTYPE html>
<html lang="en">
<head>
<meta charset="utf-8">
<title>VERO Protein Bar Wrappers</title>
<link rel="stylesheet" href="https://fonts.googleapis.com/css2?family=Roboto+Condensed:ital,wght@0,700;1,700&display=swap">
<style>
  :root {
    --bg-center: #ffffff;
    --bg-edge: #e2e2e2;
    --panel-light: #ececec;
    --panel-light-2: #d9d9d9;
    --ink: #2a2a2a;
    --white: #ffffff;
    --chip-grey: #a8a8a8;
    --strawberry: #e3131b;
    --chocolate: #4b2a17;
    --banana: #f5ae36;
  }
  * { box-sizing: border-box; margin: 0; padding: 0; }
  html, body { width: 1200px; height: 900px; overflow: hidden; }
  body {
    background: radial-gradient(ellipse at 50% 50%, var(--bg-center) 40%, var(--bg-edge) 100%);
    font-family: "Roboto Condensed", "Arial Narrow", sans-serif;
    font-weight: 700;
    position: relative;
  }
  .wrapper {
    position: absolute;
    left: 290px;
    width: 700px;
    height: 183px;
    overflow: hidden;
    background: linear-gradient(180deg, var(--panel-light), var(--panel-light-2));
    box-shadow: 0 1px 3px rgba(0,0,0,.2);
  }
  .wrapper--strawberry { top: 106px; --accent: var(--strawberry); --accent-ink: var(--white); }
  .wrapper--chocolate  { top: 362px; --accent: var(--chocolate);  --accent-ink: var(--white); }
  .wrapper--banana     { top: 618px; --accent: var(--banana);     --accent-ink: var(--ink); }

  .wrapper__swoosh { position: absolute; inset: 0; }
  .swoosh-dark { fill: url(#darkFill); }
  .swoosh-line { fill: none; stroke: var(--accent); stroke-width: 4; }

  .stat {
    position: absolute;
    border-radius: 5px;
    text-align: center;
    font-style: italic;
    line-height: 1;
    padding-top: 5px;
    box-shadow: 0 1px 3px rgba(0,0,0,.35);
  }
  .stat__value { display: block; font-size: 23px; }
  .stat__label { display: block; font-size: 8px; margin-top: -1px; }
  .stat--protein { left: 40px; top: 8px; width: 45px; height: 42px; background: var(--panel-light); color: var(--ink); }
  .stat--fat { left: 40px; top: 58px; width: 33px; height: 40px; background: var(--chip-grey); color: var(--ink); }
  .stat--sugar { left: 24px; top: 109px; width: 40px; height: 43px; background: var(--accent); color: var(--accent-ink); }

  .brand-name {
    position: absolute;
    left: 92px;
    top: 4px;
    font-size: 128px;
    font-weight: 700;
    letter-spacing: -1px;
    line-height: 1;
    white-space: nowrap;
    color: var(--ink);
  }

  .product-photo {
    position: absolute;
    left: 400px;
    top: 12px;
    width: 212px;
    height: 118px;
    border-radius: 4px;
    background: linear-gradient(90deg, #c9a775 0%, #b89360 45%, var(--accent) 100%);
  }

  .flavor-label {
    position: absolute;
    left: 445px;
    top: 132px;
    width: 150px;
    height: 18px;
    border-radius: 4px;
    background: var(--accent);
    color: var(--accent-ink);
    font-size: 12px;
    font-style: italic;
    text-align: center;
    line-height: 18px;
    white-space: nowrap;
  }

  .net-weight {
    position: absolute;
    left: 645px;
    top: 8px;
    width: 46px;
    height: 46px;
    border-radius: 5px;
    background: var(--panel-light);
    box-shadow: 0 1px 3px rgba(0,0,0,.3);
    color: var(--ink);
    font-style: italic;
    text-align: center;
    line-height: 1;
    padding-top: 4px;
  }
  .net-weight__value { display: block; font-size: 23px; }
  .net-weight__label { display: block; font-size: 8px; }

  .claims {
    position: absolute;
    right: 8px;
    top: 98px;
    list-style: none;
    text-align: right;
    color: var(--white);
    font-style: italic;
    font-size: 17px;
    line-height: 28px;
  }

  .tagline {
    position: absolute;
    left: 80px;
    top: 158px;
    color: var(--white);
    font-size: 16px;
    letter-spacing: .3px;
    white-space: nowrap;
  }
</style>
</head>
<body>
<svg width="0" height="0" style="position:absolute">
  <defs>
    <linearGradient id="darkFill" x1="0" y1="0" x2="0" y2="1">
      <stop offset="0" stop-color="#4a4a4a"/>
      <stop offset="1" stop-color="#242424"/>
    </linearGradient>
  </defs>
</svg>

<section class="wrapper wrapper--strawberry">
  <svg class="wrapper__swoosh" viewBox="0 0 700 183" aria-hidden="true">
    <path class="swoosh-dark" d="M0,88 C180,140 420,170 700,66 L700,183 L0,183 Z"/>
    <path class="swoosh-line" d="M80,118 C250,150 450,160 700,66"/>
  </svg>
  <div class="stat stat--protein"><span class="stat__value">39g</span><span class="stat__label">protein</span></div>
  <div class="stat stat--fat"><span class="stat__value">0g</span><span class="stat__label">fat</span></div>
  <div class="stat stat--sugar"><span class="stat__value">3g</span><span class="stat__label">sugar</span></div>
  <div class="brand-name">VERO</div>
  <div class="product-photo" role="img" aria-label="Peanut protein bar beside a fresh strawberry"></div>
  <div class="flavor-label">PEANUT &amp; STRAWBERRY</div>
  <div class="net-weight"><span class="net-weight__value">50g</span><span class="net-weight__label">net weight</span></div>
  <ul class="claims"><li>PROTEIN</li><li>ENERGIE</li><li>100% NATURAL</li></ul>
  <p class="tagline">PREMIUM PEANUTBASED PROTEIN BAR</p>
</section>

<section class="wrapper wrapper--chocolate">
  <svg class="wrapper__swoosh" viewBox="0 0 700 183" aria-hidden="true">
    <path class="swoosh-dark" d="M0,88 C180,140 420,170 700,66 L700,183 L0,183 Z"/>
    <path class="swoosh-line" d="M80,118 C250,150 450,160 700,66"/>
  </svg>
  <div class="stat stat--protein"><span class="stat__value">39g</span><span class="stat__label">protein</span></div>
  <div class="stat stat--fat"><span class="stat__value">0g</span><span class="stat__label">fat</span></div>
  <div class="stat stat--sugar"><span class="stat__value">3g</span><span class="stat__label">sugar</span></div>
  <div class="brand-name">VERO</div>
  <div class="product-photo" role="img" aria-label="Peanut protein bar beside stacked dark chocolate pieces"></div>
  <div class="flavor-label">PEANUT &amp; CHOCOLATE</div>
  <div class="net-weight"><span class="net-weight__value">50g</span><span class="net-weight__label">net weight</span></div>
  <ul class="claims"><li>PROTEIN</li><li>ENERGIE</li><li>100% NATURAL</li></ul>
  <p class="tagline">PREMIUM PEANUTBASED PROTEIN BAR</p>
</section>

<section class="wrapper wrapper--banana">
  <svg class="wrapper__swoosh" viewBox="0 0 700 183" aria-hidden="true">
    <path class="swoosh-dark" d="M0,88 C180,140 420,170 700,66 L700,183 L0,183 Z"/>
    <path class="swoosh-line" d="M80,118 C250,150 450,160 700,66"/>
  </svg>
  <div class="stat stat--protein"><span class="stat__value">39g</span><span class="stat__label">protein</span></div>
  <div class="stat stat--fat"><span class="stat__value">0g</span><span class="stat__label">fat</span></div>
  <div class="stat stat--sugar"><span class="stat__value">3g</span><span class="stat__label">sugar</span></div>
  <div class="brand-name">VERO</div>
  <div class="product-photo" role="img" aria-label="Peanut protein bar beside stacked banana slices"></div>
  <div class="flavor-label">PEANUT &amp; BANANA</div>
  <div class="net-weight"><span class="net-weight__value">50g</span><span class="net-weight__label">net weight</span></div>
  <ul class="claims"><li>PROTEIN</li><li>ENERGIE</li><li>100% NATURAL</li></ul>
  <p class="tagline">PREMIUM PEANUTBASED PROTEIN BAR</p>
</section>
</body>
</html>
```